New Website Design for Mesa Alta Coffee

Need a website design to be uploaded on Cartwell.com. Here are some of the sites I like:
https://grindlark.com
https://www.hollowmillcoffee.com
https://brevandcoffee.com

Coding

Coded - Design and coding required

Number of Pages Required

3 page

```html
<!DOCTYPE html>
<html lang="en">
<head>
<meta charset="utf-8">
<title>Mesa Alta Coffee</title>
<link rel="stylesheet" href="https://fonts.googleapis.com/css2?family=Alegreya:ital@1&family=Open+Sans:wght@400&display=swap">
<style>
  :root {
    --white: #ffffff;
    --ink: #111111;
    --brand-green: #23841c;
    --cart-brown: #6b3a24;
    --cta-green: #17b32a;
    --hero-top: #7a6062;
    --hero-mid: #8e6550;
    --hero-low: #5e3420;
    --hero-warm: #a9704e;
  }
  * { margin: 0; padding: 0; box-sizing: border-box; }
  html, body { width: 1200px; height: 1200px; overflow: hidden; background: var(--white); }
  .page { position: relative; width: 1200px; height: 1200px; }

  .site-header { position: absolute; left: 0; top: 0; width: 1200px; height: 136px; }
  .brand {
    position: absolute; left: 42px; top: 48px;
    font-family: "Open Sans", sans-serif; font-size: 32px; line-height: 1;
    color: var(--brand-green); white-space: nowrap;
  }
  .main-nav {
    position: absolute; left: 590px; top: 56px;
    display: flex; gap: 10px;
    font-family: "Alegreya", serif; font-style: italic; font-size: 25px; line-height: 1;
  }
  .main-nav a { color: var(--ink); text-decoration: none; }
  .menu-toggle { position: absolute; left: 1080px; top: 65px; }
  .cart-icon { position: absolute; left: 1130px; top: 53px; }

  .hero {
    position: absolute; left: 0; top: 136px; width: 1200px; height: 762px;
    background:
      radial-gradient(ellipse 45% 35% at 90% 40%, rgba(169,112,78,.7), transparent 70%),
      radial-gradient(ellipse 40% 30% at 40% 85%, rgba(94,52,32,.8), transparent 70%),
      linear-gradient(180deg, var(--hero-top) 0%, var(--hero-mid) 50%, var(--hero-low) 100%);
  }
  .hero-title {
    position: absolute; left: 657px; top: 266px;
    font-family: "Alegreya", serif; font-style: italic; font-weight: 400;
    font-size: 57px; line-height: 74px; color: var(--white);
  }
  .hero-cta {
    position: absolute; left: 657px; top: 437px; width: 154px; height: 61px;
    background: var(--cta-green); color: var(--white);
    font-family: "Alegreya", serif; font-style: italic; font-size: 31px;
    display: flex; align-items: center; justify-content: center; text-decoration: none;
  }

  .why-heading {
    position: absolute; left: 0; top: 1020px; width: 1200px; text-align: center;
    font-family: "Open Sans", sans-serif; font-weight: 400; font-size: 56px;
    letter-spacing: -1.5px; color: var(--ink); line-height: 1;
  }
</style>
</head>
<body>
<div class="page">
  <header class="site-header">
    <div class="brand">Mesa Alta Coffee</div>
    <nav class="main-nav">
      <a href="#">Subscription</a>
      <a href="#">Shop</a>
      <a href="#">Explore coffee</a>
      <a href="#">About</a>
    </nav>
    <svg class="menu-toggle" width="26" height="24" viewBox="0 0 26 24" aria-label="Menu">
      <rect x="0" y="1" width="26" height="2" fill="#111"/>
      <rect x="0" y="11" width="26" height="2" fill="#111"/>
      <rect x="0" y="21" width="26" height="2" fill="#111"/>
    </svg>
    <svg class="cart-icon" width="32" height="32" viewBox="0 0 32 32" aria-label="Cart" fill="none" stroke="#6b3a24" stroke-width="2" stroke-linecap="round" stroke-linejoin="round">
      <path d="M1 2h4l4 19h19"/>
      <path d="M7 7h23l-3 10H9"/>
      <path d="M13 7l1 10M19 7v10M25 7l-1 10M8 12h21"/>
      <circle cx="12" cy="26" r="2.5"/>
      <circle cx="25" cy="26" r="2.5"/>
    </svg>
  </header>

  <section class="hero" role="img" aria-label="Photo of a hand holding a metal cup of coffee against a warm blurred sunset landscape">
    <h1 class="hero-title">Start your day<br>Start with our coffee</h1>
    <a class="hero-cta" href="#">Shop now</a>
  </section>

  <h2 class="why-heading">Why you can think of us</h2>
</div>
</body>
</html>
```